Marlow Realty Real Estate Brokerage Recruiting Flyer

We are a real estate brokerage looking to hire more real estate agents. We need to list everything we have to offer as a company so real estate agents will join our company. this is our company website: www.Marlowrealty.example .

100% COMMISSION NO MONTHLY FEE
$450 Flat Transaction FEE

What We Offer:
24/7 Office Access
Free E & O Insurance for 1st Year
Free Online CE and PLE
Free 1,000 Business Cards
Free Professional Social Media Marketing
Free Printing, Scanning, and Copies
Free Buyer and Seller Presentation Packages
Free Filquay Cloud Based Document Management Access
Access to our Internal Brokerage Forum
Company Profit Sharing!
Private Offices Available to Rent

*Lead Generation Software with over 3,000 Leads
*10 Leads to Start
* Free Personal CRM and Website
*Restrictions and Rules apply

Company Address:
4817 Amberfield Road
Suite 512
Fairfax, VA 22194
Phone: 703-555-0147
email: info@marlowrealty.example

Target Market(s)

Real Estate Agents

Industry/Entity Type

Real Estate

Colors
0555a3
ffffff

Requirements
Must have
• 100% COMMISSION NO MONTHLY FEE
$450 Flat Transaction FEE

What We Offer:
24/7 Office Access
Free Online CE and PLE
Free 1,000 Business Cards
Company Profit Sharing!

*10 Leads to Start

Company Address:
4817 Amberfield Road
Suite 512
Fairfax, VA 22194
Phone: 703-555-0147

```html
<!DOCTYPE html>
<html lang="en">
<head>
<meta charset="utf-8">
<title>Marlow Realty – Agent Recruiting Flyer</title>
<link href="https://fonts.googleapis.com/css2?family=Open+Sans:wght@400;600;700;800&display=swap" rel="stylesheet">
<style>
  :root {
    --navy: #0a4c9e;
    --orange: #ff8500;
    --orange-dark: #8a4a10;
    --white: #ffffff;
    --ink: #1d1d1d;
    --backdrop: #e4e4e4;
    --photo-light: #d9d4cc;
    --photo-mid: #a79e93;
    --photo-dark: #5d5852;
  }
  * { box-sizing: border-box; margin: 0; padding: 0; }
  html, body { width: 707px; height: 1200px; overflow: hidden; }
  body {
    background: var(--backdrop);
    font-family: "Open Sans", Arial, sans-serif;
    position: relative;
  }
  .flyer {
    position: absolute;
    left: 0; top: 142px;
    width: 707px; height: 915px;
    background: var(--white);
    overflow: hidden;
  }
  .hero-photo {
    position: absolute; left: 0; top: 0;
    width: 707px; height: 345px;
    background: linear-gradient(160deg, var(--photo-dark) 0%, var(--photo-mid) 35%, var(--photo-light) 70%, #efece7 100%);
  }
  .shapes { position: absolute; left: 0; top: 0; }
  .headline {
    position: absolute; left: 0; top: 345px; width: 707px; height: 80px;
    display: flex; align-items: center; justify-content: center;
    color: var(--white); font-weight: 800; font-size: 60px; letter-spacing: 1px;
  }
  .fee-offer {
    position: absolute; right: 43px; top: 430px;
    text-align: right; color: var(--white); font-weight: 700; line-height: 1;
  }
  .fee-offer .no-fee { font-size: 37px; letter-spacing: 0.5px; }
  .fee-offer .flat-fee { font-size: 20.5px; font-weight: 800; margin-top: 5px; letter-spacing: 0.3px; }
  .services-title {
    position: absolute; left: 0; top: 455px; width: 246px; height: 29px;
    text-align: center; line-height: 29px; padding-right: 10px;
    color: var(--white); font-weight: 700; font-size: 18.5px;
  }
  .service-list {
    position: absolute; left: 47px; top: 510px; list-style: none;
    color: var(--ink); font-size: 13.5px; line-height: 16px;
  }
  .service-list li { position: relative; padding-left: 18px; margin-bottom: 7.3px; }
  .service-list li svg { position: absolute; left: 0; top: 3px; }
  .brand-name {
    position: absolute; left: 372px; top: 560px; width: 300px;
    display: flex; align-items: center; gap: 10px;
    color: var(--navy); font-weight: 700; font-size: 38px; white-space: nowrap;
  }
  .brand-name .mark { width: 22px; height: 22px; background: var(--navy); flex: none; }
  .perks {
    position: absolute; left: 371px; top: 678px; list-style: none;
    color: var(--navy); font-weight: 600; font-size: 13.5px; line-height: 23px;
  }
  .contact-title {
    position: absolute; left: 239px; top: 787px; width: 229px; height: 36px;
    text-align: center; line-height: 36px;
    color: var(--white); font-weight: 600; font-size: 21px;
  }
  .footer-text { position: absolute; color: var(--white); font-size: 14px; line-height: 19.5px; white-space: nowrap; }
  .address { left: 47px; top: 837px; font-style: normal; }
  .address .line, .contacts .line { display: flex; align-items: center; }
  .address .line { padding-left: 17px; position: relative; }
  .address svg { position: absolute; left: 0; top: 3px; }
  .contacts { left: 250px; top: 833px; line-height: 21px; font-size: 13.5px; }
  .contacts svg { margin-right: 7px; flex: none; }
  .licence {
    left: 482px; top: 842px; width: 189px; text-align: right;
    font-weight: 700; font-size: 13px;
  }
  .divider { position: absolute; left: 470px; top: 846px; width: 1.5px; height: 40px; background: var(--white); }
</style>
</head>
<body>
<main class="flyer">
  <div class="hero-photo" role="img" aria-label="Photo of a business handshake over a desk with documents, a pen, keys and a small wooden model house"></div>

  <svg class="shapes" width="707" height="915" viewBox="0 0 707 915" aria-hidden="true">
    <rect x="0" y="345" width="707" height="80" fill="var(--orange)"/>
    <polygon points="275,425 707,425 707,505 325,505" fill="var(--navy)"/>
    <polygon points="0,455 227,455 246,484 0,484" fill="var(--navy)"/>
    <rect x="0" y="804" width="707" height="111" fill="var(--navy)"/>
    <polygon points="214,804 225,787 239,787" fill="var(--orange-dark)"/>
    <polygon points="491,804 480,787 468,787" fill="var(--orange-dark)"/>
    <polygon points="225,787 480,787 468,823 239,823" fill="var(--orange)"/>
  </svg>

  <h1 class="headline">100% COMMISSION</h1>

  <div class="fee-offer">
    <p class="no-fee">NO MONTHLY FEE</p>
    <p class="flat-fee">$450 FLAT TRANSACTION FEE</p>
  </div>

  <h2 class="services-title">OUR SERVICES</h2>
  <ul class="service-list">
    <li><svg width="11" height="10" viewBox="0 0 11 10"><path d="M1 5.5 L4 8.5 L10 1.5" fill="none" stroke="var(--orange)" stroke-width="1.8"/></svg>24/7 Office Access</li>
    <li><svg width="11" height="10" viewBox="0 0 11 10"><path d="M1 5.5 L4 8.5 L10 1.5" fill="none" stroke="var(--orange)" stroke-width="1.8"/></svg>Free E &amp; O Insurance for 1st Year</li>
    <li><svg width="11" height="10" viewBox="0 0 11 10"><path d="M1 5.5 L4 8.5 L10 1.5" fill="none" stroke="var(--orange)" stroke-width="1.8"/></svg>Free Online CE and PLE</li>
    <li><svg width="11" height="10" viewBox="0 0 11 10"><path d="M1 5.5 L4 8.5 L10 1.5" fill="none" stroke="var(--orange)" stroke-width="1.8"/></svg>Free 1,000 Business Cards</li>
    <li><svg width="11" height="10" viewBox="0 0 11 10"><path d="M1 5.5 L4 8.5 L10 1.5" fill="none" stroke="var(--orange)" stroke-width="1.8"/></svg>Free Professional Social Media Marketing</li>
    <li><svg width="11" height="10" viewBox="0 0 11 10"><path d="M1 5.5 L4 8.5 L10 1.5" fill="none" stroke="var(--orange)" stroke-width="1.8"/></svg>Free Printing, Scanning, and Copies</li>
    <li><svg width="11" height="10" viewBox="0 0 11 10"><path d="M1 5.5 L4 8.5 L10 1.5" fill="none" stroke="var(--orange)" stroke-width="1.8"/></svg>Free Buyer and Seller Presentation Packages</li>
    <li><svg width="11" height="10" viewBox="0 0 11 10"><path d="M1 5.5 L4 8.5 L10 1.5" fill="none" stroke="var(--orange)" stroke-width="1.8"/></svg>Free Filquay Cloud Based<br>Document Management Access</li>
    <li><svg width="11" height="10" viewBox="0 0 11 10"><path d="M1 5.5 L4 8.5 L10 1.5" fill="none" stroke="var(--orange)" stroke-width="1.8"/></svg>Access to our Internal Brokerage Forum</li>
    <li><svg width="11" height="10" viewBox="0 0 11 10"><path d="M1 5.5 L4 8.5 L10 1.5" fill="none" stroke="var(--orange)" stroke-width="1.8"/></svg>Company Profit Sharing!</li>
    <li><svg width="11" height="10" viewBox="0 0 11 10"><path d="M1 5.5 L4 8.5 L10 1.5" fill="none" stroke="var(--orange)" stroke-width="1.8"/></svg>Private Offices Available to Rent</li>
  </ul>

  <div class="brand-name"><span class="mark"></span>Marlow Realty</div>

  <ul class="perks">
    <li>*Lead Generation Software with over 3,000 Leads</li>
    <li>*10 Leads to Start</li>
    <li>* Free Personal CRM and Website</li>
    <li>*Restrictions and Rules apply</li>
  </ul>

  <h2 class="contact-title">CONTACT INFO</h2>

  <address class="footer-text address">
    <span class="line"><svg width="10" height="13" viewBox="0 0 10 13"><path d="M5 12 C2 8 1 6 1 4.5 A4 4 0 0 1 9 4.5 C9 6 8 8 5 12Z" fill="none" stroke="var(--orange)" stroke-width="1.2"/><circle cx="5" cy="4.6" r="1.4" fill="none" stroke="var(--orange)" stroke-width="1"/></svg>4817 Amberfield Road</span>
    <span class="line">Suite 512</span>
    <span class="line">Fairfax, VA 22194</span>
  </address>

  <div class="footer-text contacts">
    <span class="line"><svg width="11" height="11" viewBox="0 0 11 11"><path d="M2 1 L4 1 L5 3.5 L3.8 4.5 C4.5 6 5.2 6.7 6.5 7.2 L7.5 6 L10 7 L10 9 C10 9.6 9.5 10 9 10 C4.5 9.6 1.4 6.5 1 2 C1 1.5 1.4 1 2 1Z" fill="none" stroke="var(--orange)" stroke-width="1"/></svg>703-555-0147</span>
    <span class="line"><svg width="11" height="9" viewBox="0 0 11 9"><rect x="0.5" y="0.5" width="10" height="8" fill="none" stroke="var(--orange)" stroke-width="1"/><path d="M0.5 0.5 L5.5 5 L10.5 0.5" fill="none" stroke="var(--orange)" stroke-width="1"/></svg>info@marlowrealty.example</span>
    <span class="line"><svg width="11" height="11" viewBox="0 0 11 11"><path d="M2 9 L9 2 M5 2 L9 2 L9 6" fill="none" stroke="var(--orange)" stroke-width="1.2"/></svg>www.Marlowrealty.example</span>
  </div>

  <div class="divider"></div>

  <p class="footer-text licence">LICENSED IN D.C.,<br>MARYLAND, AND VIRGINIA</p>
</main>
</body>
</html>
```